Flyer for outback tour company

Trifold flyer with a page for each tour that we offer (4 different tours) as well as a front page and a contact page.

Front page: Kestrel Treks logo + an overview of the tours on offer:
- Grand Circuit of the Village and Ridgelands
- Opalvale Showcase Tour
- Twilight Ridgelands Tour
- Subsurface Gemhunt (prospecting) Tour.

Page 2-5: description of each tour with pricing/duration.

Last page (back of brochure): contact details.
Ph: 0488 217 654
E-mail: kestreltreksoz@mailbox-example.net
Online bookings: www.kestreltreksoz-example.com.au.
Tours can also be booked directly through the reception at the Harlow Ridge Desert Lodge and the Clay Nest Inn. Please include the logos for Harlow Ridge and Clay Nest on the last page.

Target Market(s)

Travellers/tourists

Industry/Entity Type

Tourism/tour company

Font styles to use
Sans Serif

Requirements
Must have
• In regards to the pictures… the picture with the tour guide shining the torch should be on the page with the Gemhunt Tour. The other pictures of the cave tunnels should only be on the premium tour/Gemhunt Tour or front/back page.

```html
<!DOCTYPE html>
<html lang="en">
<head>
<meta charset="utf-8">
<title>Kestrel Treks – Trifold Brochure</title>
<link href="https://fonts.googleapis.com/css2?family=Roboto:wght@400;500;700;900&family=Montserrat:wght@600;700;800&display=swap" rel="stylesheet">
<style>
:root{
  --stage:#d4d4d4;
  --brown:#4a2212;
  --brown-deep:#250603;
  --orange:#c9622a;
  --white:#ffffff;
  --ink:#1a1a1a;
  --paper-grey:#cfd0d3;
}
*{margin:0;padding:0;box-sizing:border-box}
html,body{width:819px;height:1200px;overflow:hidden}
body{background:var(--stage);font-family:'Roboto',sans-serif;position:relative;color:var(--ink)}
.sheet{position:absolute;left:78px;width:663px;height:474px;display:flex;box-shadow:0 6px 14px rgba(0,0,0,.18)}
.sheet--outside{top:86px}
.sheet--inside{top:610px}
.panel{position:relative;width:221px;height:100%;overflow:hidden}
.panel--dark{background:linear-gradient(90deg,var(--brown) 0%,#3a140a 60%,var(--brown-deep) 100%);color:var(--white)}
.panel--light{background:linear-gradient(90deg,var(--white) 55%,var(--paper-grey) 100%)}
.panel--white{background:var(--white)}
.photo{position:absolute;border-radius:50%;border:5px solid var(--orange)}
.abs{position:absolute}
.tour-title{font-weight:700;color:var(--orange);line-height:1.1}
.tour-title--sm{font-size:12.5px}
.tour-title--lg{font-size:18.5px}
.facts{font-size:10.5px;line-height:1.08}
.blurb{font-size:6.8px;line-height:1.25}
.includes{font-size:11.5px;font-weight:700;margin:5px 0 4px}
.list{list-style:none;font-size:7.8px}
.list li{position:relative;padding-left:8px;margin-bottom:11px;line-height:1.2}
.list li::before{content:"";position:absolute;left:0;top:2.5px;width:4px;height:4px;border-radius:50%;background:currentColor}
.list--orange li::before{background:var(--orange)}
.brand{display:flex;align-items:center;justify-content:center;gap:6px}
.brand__dot{border-radius:50%;background:var(--orange)}
.brand__name{font-weight:700;color:var(--ink);letter-spacing:.5px}
.cover-head{left:0;right:0;top:130px;text-align:center;font-weight:900;font-size:0}
.cover-head__line{display:block}
.cover-head__explore{font-size:39px;line-height:36px;color:var(--orange)}
.cover-head__town{font-size:26px;line-height:27px}
.cover-head__with{font-size:18.5px;line-height:20px;color:var(--orange)}
.cover-head__price{font-size:17.5px;line-height:20px}
.cover-list{left:0;right:0;top:244px;text-align:center;list-style:none;font-size:7.8px;font-weight:500}
.cover-list li{margin-bottom:8px;line-height:1.1}
.partners{left:0;right:0;top:205px;display:flex;justify-content:center;align-items:center;gap:8px}
.partner-text{font-size:7px;font-weight:700;color:var(--brown)}
.badge{width:34px;height:16px;border-radius:3px}
.divider{width:1px;height:22px;background:#999}
.thanks{left:0;right:0;top:276px;text-align:center;font-weight:900;font-size:18.5px;color:var(--brown-deep)}
.call{left:0;right:0;top:378px;text-align:center;font-family:'Montserrat',sans-serif;font-weight:700;font-size:14.5px;color:var(--orange)}
.phone{left:0;right:0;top:396px;text-align:center;font-family:'Montserrat',sans-serif;font-weight:800;font-size:23px;color:var(--ink);letter-spacing:-.3px}
.postal{left:0;right:0;top:424px;text-align:center;font-family:'Montserrat',sans-serif;font-weight:600;font-size:7.6px}
.web{left:21px;width:180px;top:438px;height:16px;border-radius:8px;background:var(--orange);color:var(--white);font-size:8px;font-weight:500;display:flex;align-items:center;justify-content:center}
.justify{text-align:justify}
</style>
</head>
<body>

<section class="sheet sheet--outside">
  <div class="panel panel--dark">
    <div class="photo" style="left:31px;top:-8px;width:194px;height:194px;background:radial-gradient(circle at 50% 30%,#9bb7cf 0%,#c98a55 45%,#5b3a26 90%)" role="img" aria-label="Two glasses of sparkling wine on stony ground overlooking the desert plains"></div>
    <div class="abs" style="left:13px;top:195px;width:200px">
      <h2 class="tour-title tour-title--sm">Grand Circuit of the Village and the Ridgelands:</h2>
      <p class="facts" style="margin-top:6px">$99 adults/$75 children<br>Duration: approx. 5 hours<br>1pm start</p>
      <p class="blurb" style="margin-top:4px">This tour is designed for those who want a more personal, authentic experience. Smaller groups, bigger experience. Sit back and relax in our spacious air-conditioned 4wd vehicle as we take you places in and around Opalvale that the others can't.</p>
      <h3 class="tour-title tour-title--sm" style="margin:5px 0 6px">The Tour Includes:</h3>
      <ul class="list">
        <li>The Old Stone Underground Chapel.</li>
        <li>Modern Underground Home (dugout).</li>
        <li>The Lunar Flats</li>
        <li>The Boundary Fence</li>
        <li>The Ridgelands.</li>
        <li>Underground Mine Tour at our private claim in the opal fields (exclusive to Kestrel Treks)</li>
      </ul>
    </div>
  </div>

  <div class="panel panel--light">
    <div class="photo" style="left:-3px;top:-27px;width:192px;height:192px;background:radial-gradient(circle at 45% 45%,#6f9fd0 0%,#b97a4c 50%,#7a3f22 85%)" role="img" aria-label="Tour vehicle parked beneath a sandstone mesa seen through a rock arch"></div>
    <div class="abs partners">
      <span class="brand" style="gap:3px"><span class="brand__dot" style="width:10px;height:10px"></span><span class="partner-text">Harlow Ridge</span></span>
      <span class="divider"></span>
      <span class="badge" style="background:#1f5fa8"></span>
      <span class="divider"></span>
      <span class="badge" style="background:#8bbf3f"></span>
    </div>
    <div class="abs brand" style="left:0;right:0;top:242px">
      <span style="width:14px;height:14px;background:var(--orange)"></span>
      <span class="partner-text" style="font-size:11px">Clay Nest</span>
    </div>
    <div class="abs thanks">THANK YOU!</div>
    <div class="abs brand" style="left:0;right:0;top:318px">
      <span class="brand__dot" style="width:34px;height:34px"></span>
      <span class="brand__name" style="font-size:15px">Kestrel Treks</span>
    </div>
    <div class="abs call">CALL US NOW!</div>
    <div class="abs phone">61-488-217-654</div>
    <div class="abs postal">PO BOX 318 OPALVALE 5790, SA</div>
    <div class="abs web">www.kestreltreksoz-example.com.au.</div>
  </div>

  <div class="panel panel--dark">
    <div class="abs panel--white" style="left:0;top:0;width:221px;height:115px"></div>
    <div class="abs brand" style="left:0;right:0;top:34px">
      <span class="brand__dot" style="width:54px;height:54px"></span>
      <span class="brand__name" style="font-size:20px">Kestrel Treks</span>
    </div>
    <h1 class="abs cover-head">
      <span class="cover-head__line cover-head__explore">EXPLORE</span>
      <span class="cover-head__line cover-head__town">OPALVALE</span>
      <span class="cover-head__line cover-head__with">WITH KESTREL TREKS</span>
      <span class="cover-head__line cover-head__price">AUSTRALIA ONLY $99</span>
    </h1>
    <ul class="abs cover-list">
      <li>Grand Circuit of the Village and the Ridgelands</li>
      <li>Opalvale Showcase Tour</li>
      <li>Twilight Ridgelands Tour</li>
      <li>Subsurface Gemhunt (prospecting) Tour</li>
    </ul>
    <div class="photo" style="left:44px;top:314px;width:206px;height:206px;background:radial-gradient(circle at 50% 55%,#b4673a 0%,#7b4628 45%,#c7a98a 90%)" role="img" aria-label="Interior of an underground chapel with painted icons"></div>
  </div>
</section>

<section class="sheet sheet--inside">
  <div class="panel panel--light">
    <div class="abs" style="left:13px;top:26px;width:200px">
      <h2 class="tour-title tour-title--lg">Opalvale Showcase Tour:</h2>
      <p class="facts" style="margin-top:16px">$85 adults/ $59 children<br>Family rate (2 adults and 2 children): $270<br>Duration approx: 5 hours</p>
      <p class="blurb" style="color:var(--orange);margin-top:4px">A tour that gives you a great insight and introduction into this unique outback town and the surrounding area. Highlights include:</p>
      <h3 class="includes">The Tour Includes:</h3>
      <ul class="list list--orange">
        <li>Glimmerstone Opal Mine &amp; Museum</li>
        <li>The Old Stone Underground Chapel.</li>
        <li>The boundary fence</li>
        <li>The Lunar Flats</li>
      </ul>
    </div>
    <div class="photo" style="left:-3px;top:263px;width:206px;height:206px;background:linear-gradient(180deg,#3d4f8a 0%,#c97a4a 55%,#f0a34a 72%,#1a0d08 85%)" role="img" aria-label="Silhouette of a mining truck sign against a sunset sky"></div>
  </div>

  <div class="panel panel--dark">
    <div class="photo" style="left:-43px;top:-96px;width:304px;height:304px;background:linear-gradient(180deg,#2f6fb4 0%,#6aa0d4 45%,#c7763e 62%,#a04a22 85%)" role="img" aria-label="Colourful eroded desert hills under a blue sky"></div>
    <div class="abs" style="left:13px;top:268px;width:200px">
      <h2 class="tour-title tour-title--lg">Twilight Ridgelands Tour: $60</h2>
      <p class="facts" style="margin-top:8px">Duration approx. 3.5 hours<br>Departs 3 hours before sunset</p>
      <p class="blurb" style="margin-top:6px">A perfect way to end the day. Take in the spectacular views of the colourful Ridgelands. Watch the sun go down across the desert horizon, while enjoying a hot beverage (tea, coffee, hot chocolate) in one hand and a home-made scone in the other.</p>
      <h3 class="tour-title" style="font-size:11.5px;margin:6px 0 6px">The Tour Includes:</h3>
      <ul class="list">
        <li>The Boundary fence</li>
        <li>The Lunar Flats</li>
        <li>The Ridgelands</li>
      </ul>
    </div>
  </div>

  <div class="panel panel--white">
    <div class="abs" style="left:9px;top:18px;width:204px">
      <h2 class="tour-title tour-title--lg">Subsurface Gemhunt (prospecting) Tour: $50</h2>
      <p class="facts" style="margin-top:10px">Duration approx. 2 hours<br>9.30am start</p>
      <p class="blurb" style="margin-top:6px">This tour is ideal for those who don't mind getting down and dirty whilst searching for their own opals.</p>
      <p class="blurb justify" style="font-size:7.4px;margin-top:6px">Exclusive to Kestrel Treks, this impressive opal mine has extracted hundreds of thousands of dollars worth of opal.<br>After a quick introduction to prospecting, you will be handed a blacklight, sieve and shovel to explore the tailings in the hopes of finding your own piece of opal to take home with you.&nbsp; A truly unique experience.</p>
    </div>
    <div class="photo" style="left:10px;top:237px;width:274px;height:274px;background:radial-gradient(circle at 40% 45%,#9fb0a6 0%,#5e5548 35%,#3a2a20 75%)" role="img" aria-label="Tour guide shining a torch into an opal mine tunnel"></div>
  </div>
</section>

</body>
</html>
```